Kettle Ledger Business Card design

We need a stand out business card design for Accounting practice based in Australia specialising in pubs, clubs and hotels. We help venues maximise margins, create time and manage cashflow. One club we have been working with for the last 6 months has increased revenue by 3% and margin by 5% in this time frame. We have a back office outsourced system that costs less than having a full time employee and also allows the venues the added benefit of:<br/>-using the office space to become a revenue generating opportunity. <br/>-a complete system to enhance governance, accountability and efficiency within their operation<br/>-52 weeks cover so no hassle to cover annual/sick .. leave<br/><br/>We would like to see designs that use the colours of our logo (green & blue).
Target Market(s)
Australian Pubs, Clubs & Hotels abookkeeping, accounting and tax services
Industry/Entity Type
Accountant
Contact Information for Business Card
Miriam Oakley CPA
Principal
Accountant Tax Agent
Miriam@KettleLedger-example.com.au
0418693142
www.kettleledger-example.com.au
Accounting / Payroll / Tax / SMSF / Technology
Colors
Designer to choose colors to be used in the design.
Look and feel
Each slider illustrates characteristics of the customer's brand and the style your logo design should communicate.

```html
<!DOCTYPE html>
<html lang="en">
<head>
<meta charset="utf-8">
<title>Kettle Ledger Business Card</title>
<link rel="stylesheet" href="https://fonts.googleapis.com/css2?family=Montserrat:wght@500;700&family=Oswald:wght@500&family=Roboto:wght@400&display=swap">
<style>
  :root {
    --page-bg: #e6e6e4;
    --card-bg: #1b1b1b;
    --card-bg-deep: #141414;
    --ink: #ffffff;
    --ink-soft: #d9d9d9;
    --emboss: #2a2a2a;
    --rule: #8a8a8a;
  }
  * { margin: 0; padding: 0; box-sizing: border-box; }
  html, body { width: 1200px; height: 912px; overflow: hidden; background: var(--page-bg); }
  .sheet { position: relative; width: 1200px; height: 912px; }

  .card {
    position: absolute;
    left: 260px;
    width: 680px;
    height: 390px;
    background: linear-gradient(160deg, var(--card-bg) 0%, var(--card-bg-deep) 100%);
    box-shadow: 0 10px 28px rgba(0,0,0,0.25);
  }
  .card--back { top: 52px; }
  .card--front { top: 470px; color: var(--ink); }

  /* Back: tonal name in place of the mark */
  .back-mark {
    position: absolute;
    inset: 0;
    display: flex;
    align-items: center;
    justify-content: center;
    gap: 16px;
  }
  .back-mark__dot { width: 40px; height: 40px; border-radius: 50%; background: var(--emboss); }
  .back-mark__name {
    font-family: "Montserrat", sans-serif;
    font-weight: 700;
    font-size: 44px;
    color: var(--emboss);
  }

  /* Front */
  .brand {
    position: absolute;
    top: 56px;
    left: 0; right: 0;
    display: flex;
    justify-content: center;
    align-items: center;
    gap: 14px;
  }
  .brand__dot { width: 34px; height: 34px; border-radius: 50%; border: 2px solid var(--ink); }
  .brand__name {
    font-family: "Montserrat", sans-serif;
    font-weight: 700;
    font-size: 40px;
    letter-spacing: 0.5px;
  }

  .identity {
    position: absolute;
    top: 150px;
    left: 0; right: 0;
    display: flex;
    justify-content: center;
    align-items: center;
  }
  .person { text-align: right; padding-right: 26px; }
  .person__name {
    font-family: "Oswald", sans-serif;
    font-weight: 500;
    font-size: 30px;
    letter-spacing: 0.5px;
    text-transform: uppercase;
    line-height: 1.1;
  }
  .person__role {
    font-family: "Roboto", sans-serif;
    font-size: 17px;
    color: var(--ink-soft);
    margin-top: 4px;
  }
  .divider { width: 1px; height: 92px; background: var(--rule); }
  .contacts { list-style: none; padding-left: 22px; }
  .contacts li {
    display: flex;
    align-items: center;
    gap: 10px;
    font-family: "Roboto", sans-serif;
    font-size: 16px;
    color: var(--ink-soft);
    line-height: 26px;
  }
  .contacts svg { width: 13px; height: 13px; flex: none; }

  .services {
    position: absolute;
    bottom: 44px;
    left: 0; right: 0;
    text-align: center;
    font-family: "Montserrat", sans-serif;
    font-weight: 700;
    font-size: 27px;
  }
</style>
</head>
<body>
<main class="sheet">
  <section class="card card--back" aria-label="Card back">
    <div class="back-mark">
      <span class="back-mark__dot"></span>
      <span class="back-mark__name">Kettle Ledger</span>
    </div>
  </section>

  <section class="card card--front" aria-label="Card front">
    <div class="brand">
      <span class="brand__dot"></span>
      <span class="brand__name">Kettle Ledger</span>
    </div>

    <div class="identity">
      <div class="person">
        <p class="person__name">Miriam Oakley CPA</p>
        <p class="person__role">Principal</p>
      </div>
      <span class="divider"></span>
      <ul class="contacts">
        <li>
          <svg viewBox="0 0 16 16" fill="none" stroke="#fff" stroke-width="1.6"><path d="M4 1.5l2.5 3-1.5 2a8 8 0 0 0 4.5 4.5l2-1.5 3 2.5-1.5 2.5C7 15 1 9 1.5 3z"/></svg>
          0418693142
        </li>
        <li>
          <svg viewBox="0 0 16 16" fill="none" stroke="#fff" stroke-width="1.6"><rect x="1.5" y="3.5" width="13" height="9"/><path d="M1.5 3.5l6.5 5 6.5-5"/></svg>
          Miriam@KettleLedger-example.com.au
        </li>
        <li>
          <svg viewBox="0 0 16 16" fill="none" stroke="#fff" stroke-width="1.4"><circle cx="8" cy="8" r="6.5"/><ellipse cx="8" cy="8" rx="3" ry="6.5"/><path d="M1.5 8h13M2.5 5h11M2.5 11h11"/></svg>
          www.kettleledger-example.com.au
        </li>
      </ul>
    </div>

    <p class="services">Accounting | Payroll | Tax | SMSF | Technology</p>
  </section>
</main>
</body>
</html>
```